Zielgruppe
Ich bin selbständiger Vertriebspartner der Firma LURADI (hochwertige Reinigungsprodukte), und für eine meiner Zielgruppen 'Hundebesitzer/Hundeschulen etc' möchte ich mit zwei Produkten (Glanz Helfer Lappen, Fußmatte) einen tollen Flyer.
Aufgabenstellung
Aufgrund von Markenrechtvorgaben sind z.B. Schreibweise, Farbe des Logos etc vorgeschrieben.
Designmäßig würde ich mich über einen 'Eyecatcher' :-) freuen. Der Flyer soll die 3 A's beinhalten... anders sein als andere :-), gerne auch hinsichtlich des Formates.

```html
<!DOCTYPE html>
<html lang="de">
<head>
<meta charset="utf-8">
<title>LURADI Flyer – Glanz Helfer Lappen</title>
<link rel="stylesheet" href="https://fonts.googleapis.com/css2?family=Montserrat:wght@300;400;600;700&display=swap">
<style>
  :root {
    --bg: #e6e3cf;
    --yellow: #f7c824;
    --yellow-light: #fad641;
    --white: #ffffff;
    --ink: #3a3a3a;
    --ink-soft: #5a4a12;
    --towel-a: #c9a57a;
    --towel-b: #a8845a;
    --dog-a: #6e4a33;
    --dog-b: #a08a72;
    --dark-a: #2b2a30;
    --dark-b: #a89a8c;
    --fold: rgba(0,0,0,.07);
  }
  * { margin: 0; padding: 0; box-sizing: border-box; }
  html, body { width: 1200px; height: 929px; overflow: hidden; }
  body {
    background: var(--bg);
    font-family: "Montserrat", sans-serif;
    color: var(--ink);
    position: relative;
  }
  .flyer {
    position: absolute;
    left: 60px; top: 64px;
    width: 1080px; height: 800px;
    display: flex;
    box-shadow: 0 18px 40px rgba(0,0,0,.12);
  }
  .panel {
    position: relative;
    width: 360px; height: 800px;
    overflow: hidden;
  }
  .panel + .panel { box-shadow: inset 1px 0 0 var(--fold); }

  /* Panel 1: Einstieg */
  .panel--intro { background: linear-gradient(160deg, var(--yellow-light), var(--yellow)); }
  .intro__headline {
    position: absolute; left: 44px; top: 110px;
    font-size: 34px; font-weight: 400; line-height: 1.18; color: var(--ink);
  }
  .intro__text {
    position: absolute; left: 44px; top: 222px; width: 280px;
    font-size: 17px; font-weight: 300; line-height: 1.42; color: var(--ink-soft);
  }
  .photo-circle {
    position: absolute;
    border-radius: 50%;
    border: 9px solid var(--white);
  }
  .photo-circle--dog-rest {
    left: -30px; top: 520px; width: 440px; height: 440px;
    background: linear-gradient(150deg, #8a7a62 0%, var(--dog-a) 40%, var(--towel-b) 65%, #9a9a96 85%);
  }

  /* Panel 2: Produkt */
  .panel--product { background: var(--yellow); }
  .product__top {
    position: absolute; left: 0; top: 0; width: 360px; height: 440px;
    background: var(--white);
    border-bottom-right-radius: 26px;
  }
  .features {
    position: absolute; left: 0; top: 64px; width: 360px;
    list-style: none; text-align: center;
    font-size: 16px; font-weight: 400; line-height: 2.1; color: var(--ink);
  }
  .product__image {
    position: absolute; left: 70px; top: 215px; width: 220px; height: 150px;
    border-radius: 28px;
    background: linear-gradient(160deg, var(--towel-a), var(--towel-b));
  }
  .product__copy {
    position: absolute; left: 36px; top: 482px; width: 292px;
    font-size: 14px; font-weight: 300; line-height: 1.45; color: var(--ink-soft);
  }
  .product__name { font-weight: 700; color: var(--ink); }
  .prices {
    position: absolute; left: 36px; top: 702px; width: 292px;
    border-collapse: collapse;
    font-size: 14px; font-weight: 300; color: var(--ink-soft);
  }
  .prices td { padding: 3px 0; }
  .prices .size { width: 40px; }
  .prices .price { text-align: right; }

  /* Panel 3: Kontakt */
  .panel--contact { background: var(--white); }
  .brand {
    position: absolute; left: 0; top: 82px; width: 360px;
    text-align: center;
    font-size: 40px; font-weight: 700; letter-spacing: 3px; color: var(--ink);
  }
  .contact__box {
    position: absolute; left: 0; top: 180px; width: 360px; height: 620px;
    background: var(--yellow);
    border-top-left-radius: 22px;
  }
  .contact__text {
    position: absolute; left: 0; top: 210px; width: 360px;
    text-align: center; font-style: normal;
    font-size: 14px; font-weight: 300; line-height: 1.5; color: var(--ink-soft);
  }
  .contact__text p + p { margin-top: 12px; }
  .photo-circle--dog-towel {
    left: 40px; top: 400px; width: 440px; height: 440px;
    background: linear-gradient(200deg, var(--dark-b) 0%, #6a5d54 35%, var(--dark-a) 60%, #3a332f 100%);
  }
</style>
</head>
<body>
  <main class="flyer">
    <section class="panel panel--intro">
      <h1 class="intro__headline">Unser Profi<br>für alle Felle.</h1>
      <p class="intro__text">Fellnasen und ihre Besitzerinnen haben beim Thema Sauberkeit meistens etwas unterschiedliche Ansichten. Aber in einem Thema sind sie sich einig: Beide mögen es kuschelig weich.</p>
      <div class="photo-circle photo-circle--dog-rest" role="img" aria-label="Foto: brauner Hund liegt entspannt auf einem Pflegetuch"></div>
    </section>

    <section class="panel panel--product">
      <div class="product__top">
        <ul class="features">
          <li>Extrem saugfähig</li>
          <li>Ultraweich</li>
          <li>Sehr schnell trocknend</li>
        </ul>
        <div class="product__image" role="img" aria-label="Produktfoto: gefaltetes beiges Pflegetuch mit blauer Kante"></div>
      </div>
      <p class="product__copy"><span class="product__name">Glanz Helfer Lappen</span><br>Unser Glanz Helfer Lappen ist der perfekte Helfer nach Spaziergängen im Regen, einem Sprung ins kühle Nass oder dem Ausritt. Das extrem saugfähige und kuschelweiche Pflegetuch nimmt große Mengen an Schmutz und Wasser auf und entfernt, feucht angewendet, sogar angetrockneten Schmutz aus dem Fell.</p>
      <table class="prices">
        <tr><td class="size">S</td><td>34 x 55 cm</td><td class="price">19,90 €</td></tr>
        <tr><td class="size">M</td><td>45 x 85 cm</td><td class="price">38,90 €</td></tr>
      </table>
    </section>

    <section class="panel panel--contact">
      <div class="brand">LURADI</div>
      <div class="contact__box"></div>
      <address class="contact__text">
        <p>Ulrich Wagemann<br>Selbstständiger LURADI Vertriebspartner</p>
        <p>Birkenweg 12<br>40211 Lindenfeld</p>
        <p>0170 555 38 21<br>wagemann@luradi-mail.com<br>www.luradi-shop.com/wagemann</p>
      </address>
      <div class="photo-circle photo-circle--dog-towel" role="img" aria-label="Foto: Hund unter einem Pflegetuch eingekuschelt"></div>
    </section>
  </main>
</body>
</html>
```